Kettle Ledger Business Card design

We need a stand out business card design for Accounting practice based in Australia specialising in pubs, clubs and hotels. We help venues maximise margins, create time and manage cashflow. One club we have been working with for the last 6 months has increased revenue by 3% and margin by 5% in this time frame. We have a back office outsourced system that costs less than having a full time employee and also allows the venues the added benefit of:<br/>-using the office space to become a revenue generating opportunity. <br/>-a complete system to enhance governance, accountability and efficiency within their operation<br/>-52 weeks cover so no hassle to cover annual/sick .. leave<br/><br/>We would like to see designs that use the colours of our logo (green & blue).
Target Market(s)
Australian Pubs, Clubs & Hotels abookkeeping, accounting and tax services
Industry/Entity Type
Accountant
Contact Information for Business Card
Miriam Oakley CPA
Principal
Accountant Tax Agent
Miriam@KettleLedger-example.com.au
0418693142
www.kettleledger-example.com.au
Accounting / Payroll / Tax / SMSF / Technology
Colors
Designer to choose colors to be used in the design.
Look and feel
Each slider illustrates characteristics of the customer's brand and the style your logo design should communicate.

```html
<!DOCTYPE html>
<html lang="en">
<head>
<meta charset="utf-8">
<title>Kettle Ledger Business Card</title>
<link rel="stylesheet" href="https://fonts.googleapis.com/css2?family=Montserrat:wght@800&family=Questrial&display=swap">
<style>
  :root {
    --stage: #cccccc;
    --paper: #ffffff;
    --brand-blue: #23448c;
    --brand-green: #17763f;
    --ink: #1e1e1e;
  }
  html, body {
    margin: 0;
    width: 1200px;
    height: 1200px;
    overflow: hidden;
    background: var(--stage);
  }
  .card {
    position: absolute;
    left: 99px;
    width: 1017px;
    height: 512px;
    overflow: hidden;
  }
  .card-front {
    top: 52px;
    background: var(--paper);
    box-shadow: 0 22px 26px -14px rgba(0,0,0,0.35);
  }
  .card-back {
    top: 615px;
    background: var(--brand-blue);
  }
  .edge-bar {
    position: absolute;
    width: 38px;
    height: 114px;
  }
  .edge-bar.blue { background: var(--brand-blue); top: 143px; }
  .edge-bar.green { background: var(--brand-green); top: 257px; height: 115px; }
  .edge-bar.left { left: 0; }
  .edge-bar.right { right: 0; }

  .brand {
    position: absolute;
    display: flex;
    align-items: center;
  }
  .brand-dot {
    border-radius: 50%;
    flex: none;
  }
  .brand-name {
    font-family: "Montserrat", sans-serif;
    font-weight: 800;
    line-height: 0.95;
    letter-spacing: -0.5px;
  }
  .card-front .brand { left: 68px; top: 205px; }
  .card-front .brand-dot {
    width: 90px; height: 90px;
    background: var(--brand-green);
    margin-right: 22px;
  }
  .card-front .brand-name { color: var(--brand-blue); font-size: 44px; }

  .divider {
    position: absolute;
    left: 401px;
    top: 152px;
    width: 2px;
    height: 211px;
    background: var(--brand-blue);
  }
  .person-name {
    position: absolute;
    left: 438px;
    top: 138px;
    margin: 0;
    font-family: "Montserrat", sans-serif;
    font-weight: 800;
    font-size: 34px;
    color: var(--brand-blue);
    letter-spacing: 0.2px;
  }
  .person-role {
    position: absolute;
    left: 438px;
    top: 177px;
    margin: 0;
    font-family: "Questrial", sans-serif;
    font-size: 24px;
    color: var(--ink);
  }
  .contact {
    position: absolute;
    left: 434px;
    display: flex;
    align-items: center;
    font-family: "Questrial", sans-serif;
    font-size: 25px;
    color: var(--ink);
  }
  .contact svg { width: 30px; height: 30px; margin-right: 16px; flex: none; }
  .contact.phone { top: 231px; }
  .contact.email { top: 284px; }
  .contact.web { top: 333px; }

  .card-back .brand { left: 273px; top: 177px; }
  .card-back .brand-dot {
    width: 150px; height: 150px;
    background: var(--paper);
    margin-right: 30px;
  }
  .card-back .brand-name { color: var(--paper); font-size: 62px; }

  .service-strip {
    position: absolute;
    left: 0; right: 0;
    top: 438px;
    height: 45px;
    background: var(--paper);
    display: flex;
    justify-content: center;
    align-items: center;
    gap: 22px;
    font-family: "Questrial", sans-serif;
    font-size: 31px;
    color: var(--brand-green);
  }
</style>
</head>
<body>
  <section class="card card-front">
    <div class="edge-bar blue left"></div>
    <div class="edge-bar green left"></div>
    <div class="edge-bar blue right"></div>
    <div class="edge-bar green right"></div>

    <div class="brand">
      <span class="brand-dot"></span>
      <span class="brand-name">Kettle<br>Ledger</span>
    </div>

    <div class="divider"></div>

    <h1 class="person-name">Miriam Oakley CPA</h1>
    <p class="person-role">Principal / Accountant Tax Agent</p>

    <div class="contact phone">
      <svg viewBox="0 0 30 30" aria-hidden="true">
        <path d="M21 5c3-2 6 0 5 2l-3 1c-1-1-2-1-3 0l-6 9c-1 2 0 3 1 3l1 2c-2 2-6 1-7-1-2-3 0-7 2-10 3-3 6-5 10-6z" fill="none" stroke="var(--brand-blue)" stroke-width="2.2" stroke-linejoin="round"/>
      </svg>
      <span>0418693142</span>
    </div>
    <div class="contact email">
      <svg viewBox="0 0 30 30" aria-hidden="true">
        <rect x="2" y="6" width="26" height="18" fill="none" stroke="var(--brand-blue)" stroke-width="3"/>
        <path d="M3 8l12 9 12-9" fill="none" stroke="var(--brand-blue)" stroke-width="3"/>
      </svg>
      <span>Miriam@KettleLedger-example.com.au</span>
    </div>
    <div class="contact web">
      <svg viewBox="0 0 30 30" aria-hidden="true">
        <circle cx="15" cy="15" r="11" fill="var(--brand-blue)"/>
        <g fill="none" stroke="#ffffff" stroke-width="1">
          <ellipse cx="15" cy="15" rx="5" ry="11"/>
          <line x1="15" y1="4" x2="15" y2="26"/>
          <line x1="4" y1="15" x2="26" y2="15"/>
          <line x1="6" y1="10" x2="24" y2="10"/>
          <line x1="6" y1="20" x2="24" y2="20"/>
        </g>
      </svg>
      <span>www.kettleledger-example.com.au</span>
    </div>
  </section>

  <section class="card card-back">
    <div class="brand">
      <span class="brand-dot"></span>
      <span class="brand-name">Kettle<br>Ledger</span>
    </div>
    <div class="service-strip">
      <span>Accounting</span><span>-</span>
      <span>Payroll</span><span>-</span>
      <span>Tax</span><span>-</span>
      <span>SMSF</span><span>-</span>
      <span>Technology</span>
    </div>
  </section>
</body>
</html>
```